Single Page Production Company Site

Clean. Simple. Minimalist site with one page.

No portfolio, just some text to communicate a general overview of what the company does.

We work for a very select group of clients, creating strong brand personalities online. The site is specifically minimal and not communicating too much about what we do.. we have a variety of capabilities to work with clients and prefer to be broad with just a simple landing page as the point of contact for our brand.
Updates

Christmas holidays are coming up, maybe people need some time away from work with family and friends... We can keep working on this and I will provide feedback as quickly as possible, but I understand if designers have other commitments during the coming days. Thanks for your hard work!

Industry/Entity Type

Design Agency

Coding

Coded - Design and coding required

Number of Pages Required

1 page

Font styles to use
Sans Serif

Requirements
Must have
• Clean, bold text headlines.
Nice to have
• Unsure about any images used in the design, would like to see options with or without.

```html
<!DOCTYPE html>
<html lang="en">
<head>
<meta charset="utf-8">
<title>Crest Studio</title>
<link href="https://fonts.googleapis.com/css2?family=Nunito:wght@400;600;700&family=Roboto:wght@300;400;700&display=swap" rel="stylesheet">
<style>
:root{
  --yellow:#ecc207;
  --yellow-dark:#a8890a;
  --ink:#333;
  --ink-soft:#555;
  --muted:#888;
  --page:#f7f8fa;
  --card:#fff;
  --slate:#666;
  --footer:#353840;
  --footer-text:#6b6f7a;
  --line:#e6e6e6;
}
*{margin:0;padding:0;box-sizing:border-box}
html,body{width:1200px;height:1200px;overflow:hidden;background:#fff}
body{position:relative;font-family:'Roboto',sans-serif;color:var(--ink)}
.abs{position:absolute}

.hero{left:0;top:0;width:597px;height:605px;background:var(--yellow);overflow:hidden}
.brand{left:0;top:22px;font:700 18px 'Roboto',sans-serif;color:#3d3d3d;letter-spacing:-.5px}
.hero-art{left:228px;top:76px;width:106px;height:156px;border-radius:50%;background:radial-gradient(circle,rgba(60,60,60,.35),rgba(60,60,60,0) 70%)}
.hero-title{left:0;width:597px;text-align:center;color:#fff;font:400 92px/1 'Nunito',sans-serif;text-shadow:0 3px 0 #ddd,0 6px 8px rgba(0,0,0,.3);white-space:nowrap}
.hero-title.l1{top:285px}
.hero-title.l2{top:400px;left:-20px;width:637px}
.hero-copy{left:14px;width:569px;top:506px;text-align:center;font:400 18px/21px 'Nunito',sans-serif;color:#222}
.slide-next{left:555px;top:284px;width:42px;height:41px;background:var(--yellow-dark);display:flex;align-items:center;justify-content:center}
.slide-prev{left:0;top:284px;width:5px;height:41px;background:var(--yellow-dark)}

.side{left:597px;top:0;width:603px;height:1200px;background:var(--page);border-top:1px solid #ccc}
.tagline{left:597px;top:24px;width:630px;text-align:center;font:400 21px 'Nunito',sans-serif;letter-spacing:1.5px;color:#222}
.menu{left:1184px;top:29px}

.card{background:var(--card);box-shadow:0 1px 2px rgba(0,0,0,.04)}
.card-dark{left:630px;top:78px;width:270px;height:224px;background:var(--slate);border-radius:2px;text-align:center;color:#fff}
.card-dark .icon{width:34px;height:42px;margin:56px auto 8px;border-radius:50%;background:radial-gradient(circle at 50% 40%,#5fb6e6,#2c84c4 70%,transparent 71%)}
.card-dark h3{font:600 19px 'Nunito',sans-serif}
.card-dark p{margin-top:16px;font:400 12.5px 'Nunito',sans-serif;color:#e6e6e6}

.team{left:937px;top:92px;width:250px}
.team h2{font:400 30px 'Nunito',sans-serif;color:#222}
.team p{margin-top:30px;font:300 11px/20px 'Roboto',sans-serif;color:var(--ink-soft)}

.goal{left:630px;top:331px;width:270px;height:247px}
.goal h2{text-align:center;margin-top:10px;font:400 54px 'Nunito',sans-serif;color:#333}
.goal p{position:absolute;left:27px;top:120px;width:222px;font:300 11px/17.6px 'Roboto',sans-serif;color:#444;display:-webkit-box;-webkit-line-clamp:4;-webkit-box-orient:vertical;overflow:hidden}
.divider{position:absolute;left:12px;right:12px;height:1px;background:var(--line)}
.more{position:absolute;font:400 9px 'Roboto',sans-serif;letter-spacing:1px;color:var(--muted)}

.size{left:926px;top:286px;width:270px;height:224px;background:var(--slate);border-radius:2px;text-align:center;color:#fff;overflow:hidden}
.size-art{position:absolute;inset:0;background:radial-gradient(ellipse at 50% 60%,#5e5e5e,var(--slate) 70%)}
.size h3{position:relative;margin-top:38px;font:600 19px 'Nunito',sans-serif}
.size p{position:relative;margin:12px auto 0;width:180px;font:400 12px/22px 'Nunito',sans-serif;color:#eee}

.who{left:926px;top:538px;width:271px;height:100px}
.who h3{position:absolute;left:16px;top:14px;font:400 16px 'Nunito',sans-serif;color:#111}

.post{left:630px;top:604px;width:271px;height:66px}
.post .date{position:absolute;left:12px;top:42px;font:400 9px 'Roboto',sans-serif;color:var(--muted);display:flex;align-items:center;gap:5px}
.post .tag{position:absolute;right:12px;top:42px;font:400 9px 'Roboto',sans-serif;color:var(--muted)}

.field{background:#fff;font:400 16px 'Nunito',sans-serif;color:#777;padding:9px 11px}
.f-name{left:661px;top:726px;width:243px;height:36px}
.f-email{left:924px;top:726px;width:242px;height:36px}
.f-phone{left:661px;top:781px;width:155px;height:36px}
.f-subject{left:836px;top:781px;width:330px;height:36px}
.f-msg{left:661px;top:837px;width:505px;height:169px}
.send{left:846px;top:1050px;width:132px;height:32px;border:1.5px solid #333;border-radius:16px;text-align:center;font:400 11px/29px 'Roboto',sans-serif;letter-spacing:1.2px;color:#333}

.footer{left:630px;top:1106px;width:568px;height:94px;background:var(--footer)}
.footer p{position:absolute;left:31px;top:34px;width:240px;font:300 11px/20px 'Roboto',sans-serif;color:var(--footer-text)}
.social{position:absolute;top:32px;width:26px;height:26px;border-radius:50%}
.to-top{left:1174px;top:1154px;width:26px;height:32px;background:#222;display:flex;align-items:center;justify-content:center}
</style>
</head>
<body>

<section class="abs hero">
  <div class="abs brand">Crest Studio</div>
  <div class="abs hero-art" role="img" aria-label="Line drawing of a head in profile shaped like a light bulb"></div>
  <h1 class="abs hero-title l1">Ideas</h1>
  <h1 class="abs hero-title l2">Happen Here</h1>
  <p class="abs hero-copy">Our clients look to us for unique, exceptional solutions to their technology issues. We bring creativity to the table and solve your business’ problems with actionable solutions.</p>
  <div class="abs slide-prev"></div>
  <div class="abs slide-next"><svg width="14" height="18" viewBox="0 0 14 18"><path d="M4 3l6 6-6 6" fill="none" stroke="#fff" stroke-width="2"/></svg></div>
</section>

<div class="abs side"></div>
<div class="abs tagline">CONCEPT. CREATE. COMPLETE.</div>
<svg class="abs menu" width="10" height="9" viewBox="0 0 10 9"><path d="M0 1h10M0 4.5h10M0 8h10" stroke="#333" stroke-width="1.4"/></svg>

<div class="abs card-dark">
  <div class="icon" role="img" aria-label="Small globe icon"></div>
  <h3>Crest Studio</h3>
  <p>Concept. Create. Complete.</p>
</div>

<div class="abs team">
  <h2>The Crest Team</h2>
  <p>Crest Studio Company focuses on creating extraordinary online experiences for extraordinary clients. We'll work with you to create the perfect online presence for your brand.</p>
</div>

<article class="abs card goal">
  <h2>Our Goal</h2>
  <p>Crest Studio brings your brand to life, online. We do it all when it comes to online commerce for retail stores, wholesalers and distributors. Taking your company online introduces a world of new customers.</p>
  <div class="divider" style="top:210px"></div>
  <span class="more" style="left:12px;top:227px">VIEW MORE →</span>
</article>

<article class="abs size">
  <div class="size-art" role="img" aria-label="Faint background illustration of expanding arrows"></div>
  <h3>Size is Everything</h3>
  <p>We don't work in a massive corporate office and we don't have a mailroom. Not that there's anything wrong with that,</p>
</article>

<article class="abs card who">
  <h3>Who's Martin?</h3>
  <span class="more" style="left:13px;top:80px">VIEW MORE →</span>
</article>

<article class="abs card post">
  <div class="divider" style="top:28px"></div>
  <span class="date"><svg width="11" height="11" viewBox="0 0 11 11" fill="none" stroke="#aaa"><rect x=".5" y="1.5" width="10" height="9"/><path d="M.5 4h10M3 6h1M5 6h1M7 6h1M3 8h1M5 8h1M7 8h1"/></svg>10TH FEB 2014</span>
  <span class="tag">FOOD</span>
</article>

<div class="abs field f-name">Name</div>
<div class="abs field f-email">Email Address</div>
<div class="abs field f-phone">Phone</div>
<div class="abs field f-subject">Subject</div>
<div class="abs field f-msg">Your Message</div>
<div class="abs send">SEND MESSAGE</div>

<footer class="abs footer">
  <p>Copyrights © 2018 All Rights Reserved by Larkfield</p>
  <span class="social" style="left:418px;background:#3b5998"></span>
  <span class="social" style="left:448px;background:#1da1f2"></span>
  <span class="social" style="left:478px;background:#dd4b39"></span>
  <span class="social" style="left:508px;background:#cb2027"></span>
</footer>
<div class="abs to-top"><svg width="10" height="7" viewBox="0 0 10 7"><path d="M1 6l4-4 4 4" fill="none" stroke="#fff" stroke-width="1.5"/></svg></div>

</body>
</html>
```